Bright Harbor Construction

We are a commercial construction company specializing in steel stud framing, drywall, taping and acoustical ceilings. We would like a company logo (Something that looks great and isnt boring) as we have not been able to come up with one. A modern looking card would definitely suit our personalities best

We would like to try and avoid using dark colors. I have learned from experience that dark colors are the last to looked at. Thank you

```html
<!DOCTYPE html>
<html lang="en">
<head>
<meta charset="utf-8">
<title>Bright Harbor Construction – Business Card</title>
<link rel="stylesheet" href="https://fonts.googleapis.com/css2?family=Montserrat:wght@600;700&family=Nunito+Sans:wght@300;400&display=swap">
<style>
  :root {
    --page: #ecebe8;
    --card-white: #f4f4f4;
    --amber: #f9ae3c;
    --amber-light: #fbc06a;
    --ink-grey: #6d6e71;
    --soft-grey: #8a8b8e;
    --ghost-grey: #e7e7e7;
    --wave-grey: #7c7d80;
    --white: #ffffff;
  }
  * { box-sizing: border-box; margin: 0; padding: 0; }
  html, body {
    width: 1131px; height: 1200px; overflow: hidden;
    background: var(--page);
    font-family: "Nunito Sans", Arial, sans-serif;
  }
  .card {
    position: absolute; left: 178px;
    width: 778px; height: 446px;
    border-radius: 26px; overflow: hidden;
    box-shadow: 0 14px 26px rgba(0,0,0,0.18);
  }

  /* Front */
  .card-front { top: 100px; background: var(--card-white); }
  .ghost-name {
    position: absolute; left: 300px; top: 120px; width: 470px;
    font-family: "Montserrat", Arial, sans-serif; font-weight: 700;
    font-size: 92px; line-height: 96px; color: var(--ghost-grey);
    letter-spacing: -2px;
  }
  .holder { position: absolute; left: 60px; top: 42px; }
  .holder-name { font-size: 25px; font-weight: 400; color: var(--ink-grey); letter-spacing: 0.5px; }
  .holder-name .first { color: var(--amber); }
  .holder-role { font-size: 17px; color: var(--ink-grey); margin-top: 2px; }
  .rule { width: 54px; height: 1.5px; background: var(--soft-grey); margin-top: 26px; }
  .address {
    position: absolute; left: 60px; top: 196px;
    font-size: 19px; line-height: 26px; color: var(--ink-grey); font-style: normal;
  }
  .contacts { position: absolute; left: 60px; top: 290px; list-style: none; }
  .contacts li {
    display: flex; align-items: center; gap: 14px;
    font-size: 19px; line-height: 25px; color: var(--ink-grey);
  }
  .contacts .mark { width: 10px; height: 10px; display: inline-block; flex: none; }
  .mark-square { border: 1.5px solid var(--amber); border-radius: 2px; }
  .mark-circle { border-radius: 50%; background: var(--amber); }
  .wave { position: absolute; left: 0; top: 366px; width: 778px; height: 80px; }

  .front-brand {
    position: absolute; left: 500px; top: 252px; width: 240px; text-align: center;
  }
  .brand-square {
    display: block; margin: 0 auto;
  }
  .front-brand .brand-square {
    width: 54px; height: 54px; border: 3px solid var(--amber); border-radius: 4px;
  }
  .front-brand .brand-name {
    margin-top: 14px;
    font-family: "Montserrat", Arial, sans-serif; font-weight: 700;
    font-size: 21px; line-height: 24px; color: var(--ink-grey); letter-spacing: 0.2px;
  }
  .tagline {
    display: flex; align-items: center; justify-content: center; gap: 8px;
  }
  .tagline::before, .tagline::after { content: ""; flex: 1; height: 1.5px; background: currentColor; }
  .front-brand .tagline { font-size: 14px; color: var(--ink-grey); margin-top: 2px; }

  /* Back */
  .card-back { top: 620px; background: var(--amber); }
  .back-shapes { position: absolute; inset: 0; width: 778px; height: 446px; }
  .back-brand {
    position: absolute; left: 0; right: 0; top: 84px; text-align: center; color: var(--white);
  }
  .back-brand .brand-square {
    width: 118px; height: 118px; border: 5px solid var(--white); border-radius: 6px;
  }
  .back-brand .brand-name {
    margin-top: 40px;
    font-family: "Montserrat", Arial, sans-serif; font-weight: 700;
    font-size: 39px; line-height: 44px; letter-spacing: 0.5px;
  }
  .back-brand .tagline {
    width: 400px; margin: 4px auto 0; font-size: 25px; gap: 12px;
  }
</style>
</head>
<body>

<section class="card card-front" aria-label="Business card front">
  <div class="ghost-name" aria-hidden="true">Bright Harbor</div>

  <svg class="wave" viewBox="0 0 778 80" preserveAspectRatio="none" aria-hidden="true">
    <path d="M0 30 C200 12 400 22 560 42 C660 54 720 60 778 58 L778 80 L0 80 Z" fill="var(--amber)"/>
    <path d="M0 22 C200 4 400 14 560 34 C660 46 720 52 778 50" fill="none" stroke="var(--wave-grey)" stroke-width="4"/>
  </svg>

  <div class="holder">
    <p class="holder-name"><span class="first">MARLO</span> VENNICK</p>
    <p class="holder-role">owner</p>
    <div class="rule"></div>
  </div>

  <address class="address">48 Pier Lane,<br>3rd FL Portland,<br>ME 04101</address>

  <ul class="contacts">
    <li><span class="mark mark-square"></span>harborbuildco</li>
    <li>
      <svg class="mark" viewBox="0 0 10 10" aria-label="Email"><rect x="0" y="1.5" width="10" height="7" fill="var(--amber)"/><path d="M0 1.5 L5 5.5 L10 1.5" stroke="var(--card-white)" stroke-width="1" fill="none"/></svg>
      hello@harborbuildco.com
    </li>
    <li><span class="mark mark-circle"></span>www.harborbuildco.com</li>
  </ul>

  <div class="front-brand">
    <span class="brand-square" aria-hidden="true"></span>
    <p class="brand-name">BRIGHT HARBOR</p>
    <p class="tagline">Construction</p>
  </div>
</section>

<section class="card card-back" aria-label="Business card back">
  <svg class="back-shapes" viewBox="0 0 778 446" aria-hidden="true">
    <rect x="0" y="384" width="778" height="62" fill="var(--amber-light)" opacity="0.55"/>
    <polygon points="646,270 778,270 778,446 452,446" fill="var(--amber-light)" opacity="0.6"/>
  </svg>
  <div class="back-brand">
    <span class="brand-square" aria-hidden="true"></span>
    <p class="brand-name">BRIGHT HARBOR</p>
    <p class="tagline">Construction</p>
  </div>
</section>

</body>
</html>
```